LUMO - Visión Clara - web design and concept

Website concept - Create and develop our website design and structure. LUMO is an optical store chain, and we are looking to establish our web and digital concept. In attachment there are several pictures about our stores and our logo.

The website structure should be user friendly. Colors should be light and the design as simple and minimalist as possible. There are different variations of the logothat can be used, check the file.

The website will include optical collections and sun collections as an online store. Also, a medical menu should be considered in order for clients to schedule optometry appointments. There should also be a menu for client assistance where the clients can read about glass maintenance in our workshop.

Number of Pages Required

5+ page

Font styles to use
Serif
Sans Serif

Requirements
Must have
• Must be user-friendly and minimalist.
• Please USE PICTURES FROM THE BRANDS we sell: KORNE, BRIQO, PMS, RUNO, MAFEL
Nice to have
• Nice to inspire: ZEK glasses (see website https://ch.shopzek.example/en/)
• Nice to inspire: https://korne-eyewear.example/
• Nice to ispire: https://www.pmsworld.example/en/
Should not have
• Hysteric colors and shapes

```html
<!DOCTYPE html>
<html lang="en">
<head>
<meta charset="utf-8">
<title>LUMO · Visión Clara — Product</title>
<link href="https://fonts.googleapis.com/css2?family=Raleway:wght@400;500;600&family=Lato:wght@400;700&display=swap" rel="stylesheet">
<style>
:root{
  --ink:#111111;
  --text:#333333;
  --muted:#777777;
  --line:#e4e4e4;
  --soft:#f6f6f6;
  --price:#d0211c;
  --footer:#242424;
  --footer-text:#e8e8e8;
  --white:#ffffff;
}
*{box-sizing:border-box;margin:0;padding:0}
html,body{width:1200px;height:2586px;overflow:hidden}
body{position:relative;background:var(--white);color:var(--text);font-family:"Lato",sans-serif}
.abs{position:absolute}
.display{font-family:"Raleway",sans-serif}

/* header */
.brand{left:118px;top:40px;width:90px;text-align:center}
.brand-name{font-family:"Raleway",sans-serif;font-size:34px;letter-spacing:5px;color:var(--ink);font-weight:500}
.brand-sub{font-family:"Raleway",sans-serif;font-size:9px;letter-spacing:2px;color:var(--muted);margin-top:2px}
.nav{left:366px;top:72px;display:flex;gap:8px;font-family:"Raleway",sans-serif;font-size:12px;color:#555}
.nav a{color:inherit;text-decoration:none;padding:4px 6px}
.nav a.active{background:var(--ink);color:var(--white)}
.tools{left:996px;top:75px;display:flex;gap:18px}

.crumbs{left:121px;top:176px;font-family:"Raleway",sans-serif;font-size:17px;color:var(--ink);letter-spacing:.3px}
.crumbs span{margin:0 22px}
.crumbs b{font-weight:600}

/* product */
.hero-shot{left:121px;top:247px;width:448px;height:382px;background:radial-gradient(ellipse at 50% 50%,#7a4a2a 0 14%,#f4f2f0 38%,#f3f3f3 100%)}
.thumbs{left:121px;top:638px;display:flex;gap:11px}
.thumb{width:105px;height:98px;background:radial-gradient(ellipse at 50% 50%,#8a5a38 0 12%,#f1efed 40%,#f4f4f4 100%)}

.info{left:631px;top:244px;width:460px}
.p-title{font-family:"Raleway",sans-serif;font-size:19px;font-weight:600;color:var(--ink)}
.p-sub{font-family:"Raleway",sans-serif;font-size:15px;color:var(--ink)}
.p-price{font-size:20px;color:var(--price);margin:14px 0 0 5px}
.p-h{font-family:"Raleway",sans-serif;font-size:18px;font-weight:600;color:var(--ink);margin-top:32px}
.p-body{font-size:13.5px;line-height:17px;color:var(--text)}
.buy{left:631px;top:512px;display:flex;align-items:center}
.buy-label{font-family:"Raleway",sans-serif;font-size:19px;color:var(--ink);width:110px}
.qty{display:flex;border:1px solid var(--line);height:34px}
.qty span{width:32px;display:flex;align-items:center;justify-content:center;font-size:13px;border-right:1px solid var(--line)}
.qty span:last-child{border-right:0}
.cart-btn{margin-left:21px;width:184px;height:40px;background:var(--ink);color:var(--white);font-family:"Raleway",sans-serif;font-size:18px;display:flex;align-items:center;justify-content:center}
.wish{left:631px;top:567px;font-family:"Raleway",sans-serif;font-size:13.5px;color:#444;display:flex;align-items:center;gap:8px}
.rule{left:631px;top:598px;width:362px;height:1px;background:var(--line)}
.meta{left:631px;top:612px;font-family:"Raleway",sans-serif;color:var(--ink)}
.meta .h{font-size:19px;font-weight:500}
.meta .row{font-size:17px;margin-top:4px;display:flex;align-items:center;gap:12px}
.dot{width:10px;height:10px;border-radius:50%;display:inline-block}
.share{left:631px;top:704px;display:flex;align-items:center;gap:10px;font-family:"Raleway",sans-serif;font-size:19px;font-weight:500;color:var(--ink)}
.circ{width:34px;height:34px;border-radius:50%;background:var(--ink);display:inline-block}

.more{left:121px;top:796px;width:962px;height:197px;border:2px solid #ececec}
.more-h{height:57px;border-bottom:2px solid #ececec;padding:20px 19px;font-family:"Raleway",sans-serif;font-size:19px;font-weight:500;color:var(--ink)}
.more-b{padding:15px 27px;font-size:14px;line-height:17px}

/* related */
.sec-title{width:1200px;left:0;text-align:center;font-family:"Raleway",sans-serif;color:var(--ink)}
.related{left:118px;top:1143px;display:flex;gap:14px}
.card{width:231px;height:247px;border:1px solid #ececec;text-align:center}
.card-img{width:200px;height:100px;margin:40px auto 0}
.card-name{font-size:14px;color:var(--ink);margin-top:30px}
.card-price{font-size:13px;color:var(--ink);margin-top:4px}

/* features */
.features{left:121px;top:1491px;display:flex;gap:22px}
.feature{width:306px;height:176px;background:var(--soft);text-align:center;padding-top:36px}
.feature-t{font-family:"Raleway",sans-serif;font-size:19px;color:#333;margin-top:8px}
.feature-s{font-size:13px;color:#888;margin-top:4px}

/* newsletter */
.news-sub{font-family:"Raleway",sans-serif;font-size:14px;color:#333}
.news-form{left:322px;top:1810px;width:554px;height:36px;display:flex;border:1px solid #eee;border-radius:18px}
.news-input{flex:1;font-size:14px;color:#999;padding:9px 22px}
.news-btn{width:123px;background:var(--ink);color:var(--white);border-radius:0 18px 18px 0;font-family:"Raleway",sans-serif;font-size:15px;font-weight:600;display:flex;align-items:center;justify-content:center}

/* brands */
.brands{left:121px;top:1983px;display:flex;gap:15px}
.brand-box{width:180px;height:120px;background:var(--soft);display:flex;align-items:center;justify-content:center;font-family:"Raleway",sans-serif;font-size:20px;font-weight:500;color:var(--ink);text-align:center}
.arrow{top:2032px}

/* footer */
.footer{left:0;top:2155px;width:1200px;height:431px;background:var(--footer);color:var(--footer-text)}
.f-brand{left:130px;top:32px;text-align:center;width:70px}
.f-brand .brand-name{color:var(--white);font-size:26px;letter-spacing:3px}
.f-brand .brand-sub{color:#aaa;font-size:7px;letter-spacing:1px}
.f-line{height:3px;width:115px;background:var(--white)}
.f-about{left:121px;top:148px;width:250px;font-size:14px;line-height:19px}
.f-contact{left:121px;top:192px;font-size:14px;line-height:23px}
.f-contact div{display:flex;align-items:center;gap:10px}
.pay{left:121px;top:270px;display:flex;gap:7px}
.pay span{height:24px;padding:0 7px;background:#3a3a3a;color:var(--white);font-size:10px;font-weight:700;display:flex;align-items:center}
.f-h{font-family:"Raleway",sans-serif;font-size:14px;font-weight:500;color:var(--white)}
.f-links{list-style:none;font-size:13px;line-height:21px}
.f-links li{display:flex;align-items:center;gap:12px}
.f-links li::before{content:"";width:7px;height:7px;border-radius:50%;background:var(--white)}
.tags{display:grid;grid-template-columns:repeat(3,auto);gap:11px 11px;justify-content:start}
.tags span{border:1px solid #ccc;font-size:12px;padding:3px 11px;text-align:center}
.tags span.on{background:#000;border-color:#000}
.insta{display:grid;grid-template-columns:repeat(3,76px);gap:4px}
.insta div{height:70px}
.copy-rule{left:0;top:386px;width:1200px;height:1px;background:#4a4a4a}
.copy{left:121px;top:401px;font-size:13px;color:var(--white)}
.social{left:900px;top:397px;display:flex;gap:11px}
.social span{width:26px;height:26px;border-radius:50%;background:var(--white)}
</style>
</head>
<body>

<header>
  <div class="abs brand"><div class="brand-name">LUMO</div><div class="brand-sub">VISIÓN CLARA</div></div>
  <nav class="abs nav">
    <a href="#">Home</a><a href="#" class="active">Online store</a><a href="#">Company history</a><a href="#">Medical section</a><a href="#">Store</a><a href="#">Contact Us</a>
  </nav>
  <div class="abs tools">
    <svg width="14" height="13" viewBox="0 0 14 13"><path d="M7 12 1.5 6.5a3 3 0 0 1 5.5-4 3 3 0 0 1 5.5 4Z" fill="none" stroke="#111" stroke-width="1.5"/></svg>
    <svg width="16" height="14" viewBox="0 0 16 14"><path d="M1 1h3l2 8h8l1.5-6H5" fill="none" stroke="#111" stroke-width="1.5"/><circle cx="7" cy="12" r="1.3" fill="#111"/><circle cx="13" cy="12" r="1.3" fill="#111"/></svg>
    <svg width="14" height="14" viewBox="0 0 14 14"><circle cx="6" cy="6" r="4.2" fill="none" stroke="#111" stroke-width="1.6"/><path d="M9 9l4 4" stroke="#111" stroke-width="1.8"/></svg>
  </div>
</header>

<div class="abs crumbs">HOME<span>/</span>PRODUCTS<span>/</span><b>MARLOW ROUND LENSES</b></div>

<main>
  <div class="abs hero-shot" role="img" aria-label="Product photo: round tortoiseshell frames with gold bridge"></div>
  <div class="abs thumbs">
    <div class="thumb" role="img" aria-label="Frame front view"></div>
    <div class="thumb" role="img" aria-label="Frame angled view"></div>
    <div class="thumb" role="img" aria-label="Frame hinge detail"></div>
    <div class="thumb" role="img" aria-label="Frame side view"></div>
  </div>

  <section class="abs info">
    <div class="p-title">THE VOYAGER</div>
    <div class="p-sub">(TITANIUM/ACETATE)</div>
    <div class="p-price">$ 699.99</div>
    <div class="p-h">INSPIRATION</div>
    <p class="p-body">Lorem Ipsum is simply dummy text of the printing and typesetting industry. Lorem Ipsum has been the industry's standard dummy text ever since the 1500s, when an unknown printer took a galley of type and scrambled it to make a type specimen book. It has survived not only five centuries,</p>
  </section>

  <div class="abs buy">
    <div class="buy-label">Quantity</div>
    <div class="qty"><span>-</span><span>1</span><span>+</span></div>
    <div class="cart-btn">+ ADD TO CART</div>
  </div>
  <div class="abs wish"><svg width="13" height="12" viewBox="0 0 14 13"><path d="M7 12 1.5 6.5a3 3 0 0 1 5.5-4 3 3 0 0 1 5.5 4Z" fill="none" stroke="#111" stroke-width="1.5"/></svg>ADD TO WISHLISH</div>
  <div class="abs rule"></div>
  <div class="abs meta">
    <div class="h">AVAILABLE</div>
    <div class="row">Product Code : 000000</div>
    <div class="row">Color <span style="display:flex;gap:12px;margin-left:10px"><i class="dot" style="background:#6b2b1f"></i><i class="dot" style="background:#f1c21b"></i><i class="dot" style="background:#3aa935"></i><i class="dot" style="background:#9a9a9a"></i></span></div>
  </div>
  <div class="abs share">SHARE :<span class="circ"></span><span class="circ"></span></div>

  <section class="abs more">
    <div class="more-h">MORE INFO</div>
    <p class="more-b">Lorem Ipsum is simply dummy text of the printing and typesetting industry. Lorem Ipsum has been the industry's standard dummy text ever since the 1500s, when an unknown printer took a galley of type and scrambled it to make a type specimen book. It has survived not only five centuries,</p>
  </section>

  <h2 class="abs sec-title" style="top:1056px;font-size:25px;font-weight:400">RELATED PRODUCT</h2>
  <div class="abs related">
    <div class="card"><div class="card-img" role="img" aria-label="Black aviator sunglasses" style="background:radial-gradient(ellipse at 50% 55%,#2b2b2b 0 30%,#fff 62%)"></div><div class="card-name">Product Name</div><div class="card-price">30€</div></div>
    <div class="card"><div class="card-img" role="img" aria-label="Black aviator sunglasses" style="background:radial-gradient(ellipse at 50% 55%,#2b2b2b 0 30%,#fff 62%)"></div><div class="card-name">Product Name</div><div class="card-price">30€</div></div>
    <div class="card"><div class="card-img" role="img" aria-label="Round sunglasses with pink mirrored lenses" style="background:radial-gradient(ellipse at 50% 55%,#c98bb4 0 30%,#fff 62%)"></div><div class="card-name">Product Name</div><div class="card-price">50€</div></div>
    <div class="card"><div class="card-img" role="img" aria-label="Oversized sunglasses with gradient teal lenses" style="background:radial-gradient(ellipse at 50% 55%,#4f7f83 0 28%,#fff 62%)"></div><div class="card-name">Product Name</div><div class="card-price">30€</div></div>
  </div>

  <div class="abs features">
    <div class="feature">
      <svg width="44" height="40" viewBox="0 0 44 40"><path d="M2 20 42 3 30 37 21 25Z M21 25 42 3" fill="none" stroke="#777" stroke-width="2" stroke-linejoin="round"/></svg>
      <div class="feature-t">Free Shipping</div><div class="feature-s">Free For All Over order $ 200.00</div>
    </div>
    <div class="feature">
      <svg width="42" height="42" viewBox="0 0 42 42"><circle cx="21" cy="21" r="18" fill="none" stroke="#333" stroke-width="3" stroke-dasharray="4 2"/><circle cx="21" cy="21" r="12" fill="#333"/><path d="m21 13 2.4 5 5.4.6-4 3.7 1.1 5.3-4.9-2.7-4.9 2.7 1.1-5.3-4-3.7 5.4-.6Z" fill="#fff"/></svg>
      <div class="feature-t">Money Come Back</div><div class="feature-s">100% Money Back Guarantee</div>
    </div>
    <div class="feature">
      <svg width="42" height="42" viewBox="0 0 42 42"><circle cx="21" cy="21" r="18" fill="none" stroke="#333" stroke-width="3"/><path d="M21 10v11l-6 5" fill="none" stroke="#333" stroke-width="3"/></svg>
      <div class="feature-t">24/7 Support</div><div class="feature-s">Services Support 24/7 Fast</div>
    </div>
  </div>

  <h2 class="abs sec-title" style="top:1727px;font-size:26px;font-weight:400">Subscribe To Our Newsletter</h2>
  <div class="abs sec-title news-sub" style="top:1760px">To Receive The latest News And Update</div>
  <div class="abs news-form"><div class="news-input">Your E-Mail</div><div class="news-btn">SUBMIT</div></div>

  <h2 class="abs sec-title" style="top:1920px;font-size:25px;font-weight:400">Brands</h2>
  <svg class="abs arrow" style="left:53px" width="25" height="25" viewBox="0 0 25 25"><circle cx="12.5" cy="12.5" r="11" fill="none" stroke="#111" stroke-width="2"/><path d="M14.5 8 10 12.5 14.5 17" fill="none" stroke="#111" stroke-width="2"/></svg>
  <div class="abs brands">
    <div class="brand-box">Corvane</div>
    <div class="brand-box">Halvor Paris</div>
    <div class="brand-box">Mira Lane</div>
    <div class="brand-box">Solenne</div>
    <div class="brand-box">ODA Eyewear</div>
  </div>
  <svg class="abs arrow" style="left:1120px" width="25" height="25" viewBox="0 0 25 25"><circle cx="12.5" cy="12.5" r="11" fill="none" stroke="#111" stroke-width="2"/><path d="M10.5 8 15 12.5 10.5 17" fill="none" stroke="#111" stroke-width="2"/></svg>
</main>

<footer class="abs footer">
  <div class="abs f-brand"><div class="brand-name">LUMO</div><div class="brand-sub">visión clara</div></div>
  <div class="abs f-line" style="left:121px;top:120px"></div>
  <p class="abs f-about">Lorem Ipsum is simply dummy text ipsum is simply the dummy... ›</p>
  <div class="abs f-contact">
    <div><svg width="13" height="13" viewBox="0 0 13 13"><path d="M3 1 5 4 4 5.5a7 7 0 0 0 3.5 3.5L9 8l3 2-1 2.5C6 12 1 7 .5 2Z" fill="#fff"/></svg>Phone: 123 456 7890</div>
    <div><svg width="13" height="10" viewBox="0 0 13 10"><rect x=".5" y=".5" width="12" height="9" fill="none" stroke="#fff"/><path d="M.5.5 6.5 6l6-5.5" fill="none" stroke="#fff"/></svg>Email:info@lumo.example</div>
    <div><svg width="13" height="14" viewBox="0 0 13 14"><path d="M6.5 13S1.5 8 1.5 5a5 5 0 0 1 10 0c0 3-5 8-5 8Z" fill="#fff"/><circle cx="6.5" cy="5" r="1.8" fill="#242424"/></svg>Address : 12th Street, City .Usa</div>
  </div>
  <div class="abs pay"><span>Payvo</span><span>Shopra</span><span>Walletix</span><span>Cardo</span><span>Novia</span></div>

  <div class="abs" style="left:412px;top:87px">
    <div class="f-h">INFORMATION</div>
    <div class="f-line" style="width:80px;margin:12px 0 20px"></div>
    <ul class="f-links"><li>Home</li><li>Woman</li><li>Men</li><li>Kids</li><li>Testimonials</li><li>Blogs</li><li>Contact us</li></ul>
  </div>
  <div class="abs" style="left:600px;top:87px">
    <div class="f-h">POPULAR TAGE</div>
    <div class="f-line" style="width:80px;margin:12px 0 20px"></div>
    <div class="tags"><span>Kids</span><span>Men</span><span>Lady</span><span>Woman</span><span>Latest</span><span>Specials</span><span>Faishion</span><span>Eye</span><span>offers</span><span class="on">Faishion</span><span>COOL</span></div>
  </div>
  <div class="abs" style="left:846px;top:87px">
    <div class="f-h">INSTAGRAM</div>
    <div class="f-line" style="width:80px;margin:12px 0 20px"></div>
    <div class="insta">
      <div role="img" aria-label="Gallery photo: eyewear style" style="background:#8a7565"></div>
      <div role="img" aria-label="Gallery photo: eyewear style" style="background:#9d8a7e"></div>
      <div role="img" aria-label="Gallery photo: eyewear style" style="background:#b3756a"></div>
      <div role="img" aria-label="Gallery photo: eyewear style" style="background:#a59a8f"></div>
      <div role="img" aria-label="Gallery photo: eyewear style" style="background:#8d7f74"></div>
      <div role="img" aria-label="Gallery photo: eyewear style" style="background:#a3968b"></div>
    </div>
  </div>

  <div class="abs copy-rule"></div>
  <div class="abs copy">CopyRight ©2018 LUMO Visión Clara. All Right Reserve</div>
  <div class="abs social"><span></span><span></span><span></span><span></span><span></span></div>
</footer>

</body>
</html>
```